Building Maintenance Flyer specialising in hot and silent pressure cleaning

Hi. I love this flyer. I would like something similar but with hot water pressure washing and building maintenance

Ferro Lane & Services provides high pressure steam cleaning and water blasting services throughout Brisbane and surrounding areas, covering the Industrial, Commercial, Strata and Residential property owners sectors.

FLS combining the cleaning power of heat with state-of-the-art silent equipment, accredited technicians and a steadfast commitment to the environment. We offer the best Prompt, Professional Service.

Fully Accredited & Certified Technicians
100% Satisfaction Guaranteed
We are a family owned and operated business and love what we do. No job is too big or too small and we take pride in our work.
All of our services are undertaken using industry leading equipment and, providing safe and superior results.

Our business is covered by 20 million full public liability insurance and we operate within strict health & safety guidelines, providing all our clients with complete peace of mind. Project plans and risk assessments can also be provided upon request.

BODY CORPORATES

BUILDING FAÇADE CLEANING

CAR PARKS – underground, single and multi level

DRIVE THRU

FOOD PRODUCTION FACILITIES CLEANING SANITISING

SHOPPING CENTRES

BIRD MANAGEMENT AND DECONTAMINATION

GENERAL MAINTENANCE

CONSTRUCTION CLEAN UPS

SPILL MANAGEMENT

CONCRETE CLEANING AND DEGRASING

CONCRETE SEALING

FACTORY CLEANING & CLEAN UP

ENVIRONMENTAL DECONTAMINATION OF HEAVY VEHICLES AND EQUIPMENT

SITE CLEANS AND RUBBISH REMOVAL

MANUFACTURING PLANTS

Target Market(s)

Facility Managers, Commercial and Industrial Property Owners, Property Managers, Schools, Restaurants,

Industry/Entity Type

Pressure Cleaning

Font styles to use
Sans Serif

Colors
0293ce
00a990
33a6d7
33b8a4

Requirements
Must have
• SILENT HOT WATER PRESSURE CLEANING
Runs up to 120 Degrees Celsius
SANITISING - Bin areas, outdoor areas, cafe's, restaurants, schools, drive thru's
Blue's and Greens to link in with our logo

```html
<!DOCTYPE html>
<html lang="en">
<head>
<meta charset="utf-8">
<title>Ferro Lane & Services – Commercial Flyer</title>
<link rel="stylesheet" href="https://fonts.googleapis.com/css2?family=Montserrat:wght@500;600;700;800&display=swap">
<style>
  :root{
    --blue:#0293ce;
    --blue-deep:#1a6fb8;
    --blue-soft:#33a6d7;
    --teal:#00a990;
    --teal-soft:#33b8a4;
    --grey-text:#5f6268;
    --grey-bg:#e9eaec;
    --white:#ffffff;
    --navy:#2b3158;
  }
  *{box-sizing:border-box;margin:0;padding:0}
  html,body{width:1200px;height:1000px;overflow:hidden}
  body{background:#dcdddf;font-family:"Montserrat",Arial,sans-serif;position:relative}
  .flyer{position:absolute;left:50px;top:111px;width:1100px;height:778px;overflow:hidden;background:var(--grey-bg);box-shadow:0 6px 24px rgba(0,0,0,.18)}
  .flyer-shapes{position:absolute;inset:0}
  .brand{position:absolute;left:735px;top:36px;display:flex;align-items:center;gap:10px}
  .brand-dot{width:26px;height:26px;border-radius:50%;background:var(--teal)}
  .brand-name{font-weight:800;font-size:20px;color:var(--blue-deep);letter-spacing:.5px}
  .headline{position:absolute;left:600px;top:112px;width:450px;text-align:right;font-weight:800;font-size:44px;line-height:1;color:var(--grey-text);text-transform:uppercase}
  .headline .accent{color:var(--blue-deep)}
  .tagline{position:absolute;left:600px;top:214px;width:450px;text-align:right;font-weight:700;font-size:16px;line-height:1.2;color:var(--grey-text)}
  .features{position:absolute;left:770px;top:272px;list-style:none}
  .feature{display:flex;align-items:center;gap:16px;margin-bottom:26px;font-weight:700;font-size:15px;line-height:1.15;color:var(--grey-text)}
  .feature svg{width:40px;height:40px;flex:none}
  .contact{position:absolute;left:720px;top:628px;width:340px;text-align:right;color:var(--grey-text)}
  .contact-call{font-weight:800;font-size:21px}
  .contact-call span{color:var(--blue-deep)}
  .contact-email{font-weight:500;font-size:18px;margin-top:2px}
  .contact-web{font-weight:800;font-size:19px;color:var(--blue-deep);margin-top:4px}
  .solutions{position:absolute;left:40px;top:560px;color:var(--white)}
  .solutions-title{font-weight:700;font-size:30px;letter-spacing:5px;margin-bottom:18px}
  .solutions-list{list-style:none;display:grid;grid-template-columns:220px 220px;column-gap:16px;row-gap:11px}
  .solutions-list li{display:flex;align-items:center;gap:10px;font-weight:600;font-size:13px;white-space:nowrap}
  .solutions-list svg{width:20px;height:20px;flex:none}
</style>
</head>
<body>
<main class="flyer">
  <svg class="flyer-shapes" viewBox="0 0 1100 778" width="1100" height="778">
    <defs>
      <linearGradient id="washPhoto" x1="0" y1="0" x2="1" y2="1">
        <stop offset="0" stop-color="#7f9fc8"/>
        <stop offset=".45" stop-color="#c9d3dc"/>
        <stop offset="1" stop-color="#eef1f4"/>
      </linearGradient>
      <linearGradient id="workerPhoto" x1="0" y1="0" x2="0" y2="1">
        <stop offset="0" stop-color="#4b5b92"/>
        <stop offset="1" stop-color="#262b4c"/>
      </linearGradient>
      <radialGradient id="panel" cx=".55" cy=".4" r=".7">
        <stop offset="0" stop-color="#ffffff"/>
        <stop offset="1" stop-color="#e6e7e9"/>
      </radialGradient>
    </defs>
    <rect width="1100" height="778" fill="#eceded"/>
    <rect x="0" y="0" width="620" height="560" fill="url(#washPhoto)" role="img" aria-label="Photo of a worker in blue rubber boots pressure washing a wet floor"/>
    <circle cx="865" cy="180" r="400" fill="none" stroke="var(--teal-soft)" stroke-width="22"/>
    <circle cx="862" cy="174" r="384" fill="none" stroke="var(--blue)" stroke-width="20"/>
    <circle cx="860" cy="170" r="372" fill="url(#panel)"/>
    <path d="M0,486 C190,428 440,418 700,478 L700,778 L0,778 Z" fill="var(--teal-soft)" opacity=".55"/>
    <path d="M0,508 C200,456 440,448 700,504 L700,778 L0,778 Z" fill="var(--blue)"/>
    <rect x="535" y="250" width="160" height="528" rx="56" fill="url(#workerPhoto)" role="img" aria-label="Photo of a technician in navy overalls and hard hat holding a pressure washer lance"/>
    <circle cx="390" cy="420" r="66" fill="var(--blue-deep)" stroke="#ffffff" stroke-width="6"/>
    <circle cx="390" cy="420" r="49" fill="none" stroke="#ffffff" stroke-width="2"/>
  </svg>

  <div class="brand">
    <span class="brand-dot"></span>
    <span class="brand-name">Ferro Lane &amp; Services</span>
  </div>

  <h1 class="headline"><span class="accent">All</span> Commercial<br>and Property</h1>
  <p class="tagline">FLS – servicing Southeast’s Commercial<br>&amp; Industrial sector 24/7</p>

  <ul class="features">
    <li class="feature">
      <svg viewBox="0 0 40 40" fill="none" stroke="#1a6fb8" stroke-width="2.5"><circle cx="20" cy="22" r="14"/><path d="M20 4v4M14 5h12M20 22l6-6"/></svg>
      <span>We operate 24/7<br>7 days a week</span>
    </li>
    <li class="feature">
      <svg viewBox="0 0 40 40" fill="none" stroke="#1a6fb8" stroke-width="2.5"><circle cx="20" cy="20" r="14"/><path d="M8 32L32 8"/></svg>
      <span>SILENT HOT WATER<br>pressure cleaning<br>120 degrees</span>
    </li>
    <li class="feature">
      <svg viewBox="0 0 40 40" fill="none" stroke="#1a6fb8" stroke-width="2.5"><circle cx="20" cy="20" r="10"/><path d="M20 4v6M20 30v6M4 20h6M30 20h6M9 9l4 4M27 27l4 4M31 9l-4 4M9 31l4-4"/></svg>
      <span>COVID-19 Trained</span>
    </li>
  </ul>

  <div class="contact">
    <p class="contact-call">CALL US <span>+00 0 0000 0000</span></p>
    <p class="contact-email">email@website.com</p>
    <p class="contact-web">www.website.com</p>
  </div>

  <section class="solutions">
    <h2 class="solutions-title">SOLUTIONS FOR...</h2>
    <ul class="solutions-list">
      <li><svg viewBox="0 0 20 20" fill="none" stroke="#fff" stroke-width="1.6"><circle cx="10" cy="10" r="5"/><path d="M10 1v4M10 15v4M1 10h4M15 10h4"/></svg>COVID-19 Infection Control</li>
      <li><svg viewBox="0 0 20 20" fill="none" stroke="#fff" stroke-width="1.6"><rect x="2" y="6" width="16" height="9" rx="2"/><path d="M5 15v3M15 15v3"/></svg>Common Area Cleaning</li>
      <li><svg viewBox="0 0 20 20" fill="none" stroke="#fff" stroke-width="1.6"><circle cx="10" cy="10" r="8"/><path d="M6 10l3 3 5-6"/></svg>Building Management</li>
      <li><svg viewBox="0 0 20 20" fill="none" stroke="#fff" stroke-width="1.6"><path d="M3 17C8 12 12 6 17 3M6 14c4 0 8-3 9-8"/></svg>Bird waste removal</li>
      <li><svg viewBox="0 0 20 20" fill="none" stroke="#fff" stroke-width="1.6"><path d="M4 5h12M8 5V3h4v2M5 5l1 13h8l1-13"/></svg>Bin Cleaning &amp; Sanitisation</li>
      <li><svg viewBox="0 0 20 20" fill="none" stroke="#fff" stroke-width="1.6"><rect x="4" y="3" width="12" height="15" rx="1"/><path d="M7 7h6M7 11h6"/></svg>Oil and Grease elimination</li>
      <li><svg viewBox="0 0 20 20" fill="none" stroke="#fff" stroke-width="1.6"><circle cx="10" cy="8" r="4"/><path d="M10 12v7"/></svg>Garden Maintenance</li>
      <li><svg viewBox="0 0 20 20" fill="none" stroke="#fff" stroke-width="1.6"><circle cx="6" cy="7" r="3"/><circle cx="14" cy="13" r="3"/><circle cx="14" cy="5" r="1.5"/></svg>Mould &amp; Mildew removal</li>
    </ul>
  </section>
</main>
</body>
</html>
```